New furniture company needs a cool, fresh Website - think lounjo.com, velmora.com

Tuftwell.com: We are launching a home (Storvane) furniture business, aimed at the young, discerning mid-market consumer. The aim is to compete with many furniture e-tailers, as well as more established retail brands.
We want the website to capture the hearts, minds and wallets of the target audience, placing Tuftwell.com firmly into the market place. Please look to Velmora.com for look and feel inspiration. We will be selling approx 15 products to start. I suggest using Storvane with the following theme please: – Hearth & Meadow – Radiance – Belmont. Please see the logo below. The website needs to have a sophisticated feel for affordable aspirational furniture. Soft colours and homely text - please go with look and feel of Velmora.com. Please see a below file containing image of some sofas, chairs and footstools that will be for sale.
Many thanks

Target Market(s)

mid-market, young families looking for cool, affordable, easy to buy furniture

Industry/Entity Type

Furniture

Coding

Coded - Design and coding required

Number of Pages Required

5+ page

Font styles to use
Sans Serif

Colors
86cae7
cee9f5
3277b5
eaf2ce
fdf9ce
fff3d1
0255a3
e8e8e8
cbcbcb

Requirements
Must have
• Storvane
• http://www.velmora.com/hartwick-leather-large-sofa.html - great example of what we need it to look like
• logo as shown
• homepage
• products menu - sofas, seating, footstools, antique
• images of all products (examples provided) with ability to click on various fabric swatch samples and see the sofa in different fabrics and colours (check out lounjo.com)
• facility for social media
• facility to buy online
• "add to wishlist"
• "add to basket"
Nice to have
• I want it to have a light and airy feel, nothing too heavy or corporate. Needs to be very easily navigated and a simple approach
Should not have
• Dark, heavy colours

```html
<!DOCTYPE html>
<html lang="en">
<head>
<meta charset="utf-8">
<title>Tuftwell — Furniture Store</title>
<link href="https://fonts.googleapis.com/css2?family=Roboto:wght@300;400;500;700&display=swap" rel="stylesheet">
<style>
:root{
  --sky:#86cae7;
  --sky-pale:#cee9f5;
  --blue:#3277b5;
  --navy:#0255a3;
  --cream:#fff3d1;
  --line:#e8e8e8;
  --line-dark:#cbcbcb;
  --ink:#1c1c1c;
  --text:#4a4a4a;
  --muted:#8a8a8a;
  --star:#f0a020;
  --price:#5aaee0;
}
*{box-sizing:border-box;margin:0;padding:0}
html,body{width:1200px;height:2423px;overflow:hidden;background:#fff}
body{font-family:'Roboto',Arial,sans-serif;color:var(--ink);position:relative}
.abs{position:absolute}

/* top bar */
.topbar{left:0;top:0;width:1200px;height:40px;border-bottom:1px solid var(--line);font-size:11px;color:var(--text)}
.topbar .locale{left:89px;top:13px;display:flex;gap:22px}
.topbar .locale span{display:flex;align-items:center;gap:6px}
.flag{width:14px;height:9px;background:linear-gradient(#c33 0 33%,#fff 33% 66%,#c33 66%);position:relative}
.flag::before{content:"";position:absolute;left:0;top:0;width:6px;height:5px;background:#2b4c9a}
.topbar .account{right:89px;top:13px;display:flex;gap:30px;text-transform:uppercase;letter-spacing:.3px}

/* header */
.header{left:0;top:40px;width:1200px;height:78px}
.logo{left:86px;top:14px;display:flex;flex-direction:column;align-items:center;gap:4px}
.logo-mark{width:30px;height:24px;border:1.5px solid #999;border-radius:4px}
.logo-name{font-size:13px;letter-spacing:3px;color:#888;font-weight:400}
.nav{right:203px;top:34px;display:flex;gap:24px;font-size:11px;font-weight:400;text-transform:uppercase}
.nav .active{color:var(--price);position:relative}
.nav .active::before{content:"";position:absolute;left:-14px;right:-14px;top:-35px;height:2px;background:var(--price)}
.header-tools{right:89px;top:28px;display:flex;align-items:center;gap:16px}
.header-tools .sep{width:1px;height:26px;background:var(--line-dark)}
.cart-count{position:absolute;right:-6px;top:-4px;width:13px;height:13px;border-radius:50%;background:#333;color:#fff;font-size:8px;text-align:center;line-height:13px}

/* hero */
.hero{left:0;top:118px;width:1200px;height:514px;background:linear-gradient(110deg,#e9e6e2 0%,#cfc8c0 25%,#8a7e74 45%,#6b4a38 60%,#7a5540 80%,#4a3328 100%)}
.hero-copy{left:716px;top:338px;color:#fff}
.hero-copy .kicker{font-size:20px;font-weight:400;letter-spacing:.5px}
.hero-copy h1{font-size:42px;font-weight:400;line-height:44px;margin-top:2px}
.hero-copy h1 b{font-weight:700}
.hero-copy .sub{font-size:17px;font-weight:500;margin-top:2px}
.btn-more{display:inline-block;margin-top:15px;width:121px;height:39px;background:var(--cream);color:var(--ink);font-size:11px;font-weight:500;text-align:center;line-height:39px;text-transform:uppercase}
.hero-arrow{top:342px;width:32px;height:68px;background:rgba(120,120,120,.7);display:flex;align-items:center;justify-content:center}
.dots{left:580px;top:576px;display:flex;gap:6px}
.dots i{width:10px;height:10px;border-radius:50%;border:1.5px solid #fff}
.dots i.on{background:#fff}

/* perks */
.perks{left:0;top:680px;width:1200px;height:213px}
.perk{position:absolute;top:0;width:340px;height:213px;text-align:center}
.perk svg{margin-top:58px}
.perk h3{font-size:17px;font-weight:500;text-transform:uppercase;margin-top:10px}
.perk p{font-size:12px;color:var(--text);margin-top:3px}
.perk-divider{position:absolute;top:0;width:1px;height:213px;background:var(--line)}

/* categories */
.categories{left:0;top:942px;width:1200px;height:327px;display:flex}
.category{width:300px;height:327px;position:relative;display:flex;align-items:center;justify-content:center}
.category span{color:#fff;font-size:26px;font-weight:500;text-transform:uppercase;margin-top:-12px}
.cat-sofas{background:linear-gradient(180deg,#e8eaeb,#d9dcdd 70%,#a08878)}
.cat-seating{background:linear-gradient(180deg,#eef0f1,#dcdfe1 60%,#c8cbcd)}
.cat-footstools{background:linear-gradient(180deg,#b4b6b6,#9a9c9c 60%,#8c8e8e)}
.cat-antique{background:linear-gradient(180deg,#e6e8e9,#c9cccd 60%,#a2a5a7)}

/* products */
.section-title{left:0;top:1350px;width:1200px;text-align:center;font-size:31px;font-weight:400;text-transform:uppercase}
.product{position:absolute;top:1411px;width:250px}
.product-img{width:250px;height:265px;background:#efefef;display:block}
.product.featured .product-img{background:linear-gradient(180deg,#c4ad8e,#a88d6e 60%,#7b6450);box-shadow:0 8px 18px rgba(0,0,0,.25)}
.product h4{font-size:13px;font-weight:500;text-transform:uppercase;margin-top:21px}
.stars{display:flex;gap:2px;margin-top:3px}
.price{font-size:14px;color:var(--price);margin-top:3px}
.zoom{position:absolute;left:193px;top:217px;width:38px;height:38px;background:#fff;display:flex;align-items:center;justify-content:center}
.slide-arrow{top:1518px;width:31px;height:68px;background:#a9a9a9;display:flex;align-items:center;justify-content:center;z-index:2}

/* partners */
.rule{left:89px;top:1815px;width:1022px;height:1px;background:var(--line)}
.badge{position:absolute;top:1865px;width:74px;height:74px;border:2px solid var(--line-dark);border-radius:50%}
.badge.square{border-radius:6px;width:70px;height:60px;top:1872px}

/* newsletter */
.newsletter{left:0;top:1985px;width:1200px;height:106px;background:var(--sky)}
.newsletter h2{position:absolute;left:89px;top:38px;color:#fff;font-size:25px;font-weight:400;text-transform:uppercase;letter-spacing:.3px}
.newsletter form{position:absolute;left:680px;top:32px;display:flex}
.newsletter .field{width:316px;height:44px;background:#fff;font-size:12px;color:#aaa;padding:0 20px;line-height:44px}
.newsletter .submit{width:115px;height:44px;background:var(--blue);color:#fff;font-size:12px;text-align:center;line-height:44px;text-transform:uppercase}

/* footer */
.footer-col{position:absolute;top:2153px}
.footer-col h5{font-size:13px;font-weight:500;text-transform:uppercase;margin-bottom:14px}
.footer-col li{list-style:none;font-size:11.5px;color:var(--text);height:27.5px}
.social li{display:flex;align-items:center;gap:10px;height:30px}
.social .dot{width:22px;height:22px;border-radius:50%}
.footer-rule{left:89px;top:2369px;width:1022px;height:1px;background:var(--line)}
.copyright{left:91px;top:2390px;font-size:11.5px;color:var(--text)}
.cards{left:799px;top:2384px;display:flex;gap:12px}
.card{width:42px;height:26px;border:1px solid var(--line-dark);border-radius:3px;font-size:7.5px;font-weight:500;color:var(--ink);display:flex;align-items:center;justify-content:center;white-space:nowrap}
</style>
</head>
<body>

<div class="abs topbar">
  <div class="abs locale">
    <span><i class="flag"></i>English ▾</span>
    <span>USD ▾</span>
  </div>
  <div class="abs account">
    <span>Sitemap</span><span>My Wishlist</span><span>My Account</span><span>My Cart</span><span>Sign In</span>
  </div>
</div>

<header class="abs header">
  <div class="abs logo"><i class="logo-mark"></i><span class="logo-name">TUFTWELL</span></div>
  <nav class="abs nav">
    <span class="active">Home</span><span>Categories</span><span>Products</span><span>Features</span><span>Blog</span><span>About Us</span>
  </nav>
  <div class="abs header-tools">
    <svg width="18" height="18" viewBox="0 0 18 18" fill="none" stroke="#5aaee0" stroke-width="1.6"><circle cx="7.5" cy="7.5" r="5.5"/><path d="M11.5 11.5 16 16"/></svg>
    <i class="sep"></i>
    <span style="position:relative">
      <svg width="18" height="20" viewBox="0 0 18 20" fill="none" stroke="#5aaee0" stroke-width="1.5"><path d="M2 6h14l-1 13H3z"/><path d="M6 8V4a3 3 0 0 1 6 0v4"/></svg>
      <b class="cart-count">0</b>
    </span>
  </div>
</header>

<section class="abs hero" role="img" aria-label="Living room with a brown corner sofa, cushions, wall-mounted TV on a wood-panelled wall and a patterned rug"></section>
<div class="abs hero-arrow" style="left:0"><svg width="8" height="10" viewBox="0 0 8 10"><path d="M6 1 2 5l4 4" stroke="#fff" stroke-width="1.5" fill="none"/></svg></div>
<div class="abs hero-arrow" style="right:0"><svg width="8" height="10" viewBox="0 0 8 10"><path d="M2 1l4 4-4 4" stroke="#fff" stroke-width="1.5" fill="none"/></svg></div>
<div class="abs hero-copy">
  <div class="kicker">EXTRA 20% OFF</div>
  <h1><b>SOFFA</b> COLLECTION</h1>
  <div class="sub">THE BEST SOFA COLLECTION STORE</div>
  <span class="btn-more">Learn More</span>
</div>
<div class="abs dots"><i></i><i class="on"></i><i></i></div>

<section class="abs perks">
  <div class="perk" style="left:90px">
    <svg width="48" height="48" viewBox="0 0 48 48" fill="var(--blue)"><rect x="6" y="16" width="36" height="9" rx="1"/><rect x="9" y="27" width="30" height="19" rx="1"/><rect x="22" y="16" width="4" height="30" fill="#fff"/><path d="M24 15c-4-8-12-9-12-3 0 3 6 3 12 3zm0 0c4-8 12-9 12-3 0 3-6 3-12 3z"/></svg>
    <h3>Recieve Gift Cart</h3>
    <p>Reciever gift all over oder $40</p>
  </div>
  <i class="perk-divider" style="left:430px"></i>
  <div class="perk" style="left:430px">
    <svg width="80" height="48" viewBox="0 0 80 48" fill="none" stroke="var(--sky)" stroke-width="2.5"><path d="M18 12h34v24H18zM52 20h12l8 9v7H52z"/><circle cx="28" cy="38" r="5" fill="#fff"/><circle cx="62" cy="38" r="5" fill="#fff"/><path d="M2 18h12M6 24h10M2 30h12"/></svg>
    <h3>Fast Free Shipment</h3>
    <p>For standard order over $200</p>
  </div>
  <i class="perk-divider" style="left:770px"></i>
  <div class="perk" style="left:770px">
    <svg width="48" height="48" viewBox="0 0 48 48" fill="none" stroke="#f5d98a" stroke-width="3"><path d="M9 28v-6a15 15 0 0 1 30 0v6"/><rect x="6" y="26" width="7" height="12" rx="2" fill="#f5d98a"/><rect x="35" y="26" width="7" height="12" rx="2" fill="#f5d98a"/><path d="M38 38c0 5-5 7-11 7"/></svg>
    <h3>24/7 Support</h3>
    <p>Feel free to Contact us</p>
  </div>
</section>

<section class="abs categories">
  <div class="category cat-sofas" role="img" aria-label="White chaise sofa with cushions in a bright room"><span>Sofas</span></div>
  <div class="category cat-seating" role="img" aria-label="White dining table with black chairs"><span>Seating</span></div>
  <div class="category cat-footstools" role="img" aria-label="Black tall footstool against a grey wall"><span>Footstools</span></div>
  <div class="category cat-antique" role="img" aria-label="Black leather armchair beside a grey sofa"><span>Antique</span></div>
</section>

<h2 class="abs section-title">Our Customers Love</h2>

<article class="product" style="left:89px">
  <span class="product-img" role="img" aria-label="Light grey three-seat sofa"></span>
  <h4>Bluebell Range</h4>
  <div class="stars"><svg width="60" height="10" viewBox="0 0 60 10" fill="var(--star)"><path id="st" d="M5 0l1.5 3.3 3.5.3-2.7 2.3.8 3.5L5 7.6 1.9 9.4l.8-3.5L0 3.6l3.5-.3z"/><use href="#st" x="12"/><use href="#st" x="24"/><use href="#st" x="36"/><use href="#st" x="48"/></svg></div>
  <div class="price">$25.99</div>
</article>
<article class="product" style="left:346px">
  <span class="product-img" role="img" aria-label="Olive green velvet sofa"></span>
  <h4>Yanna Range</h4>
  <div class="stars"><svg width="60" height="10" viewBox="0 0 60 10" fill="var(--star)"><use href="#st"/><use href="#st" x="12"/><use href="#st" x="24"/><use href="#st" x="36"/><use href="#st" x="48"/></svg></div>
  <div class="price">$18.99</div>
</article>
<article class="product featured" style="left:606px">
  <span class="product-img" role="img" aria-label="Grey sofa in front of a rustic wooden wall"></span>
  <span class="zoom"><svg width="12" height="12" viewBox="0 0 12 12" fill="none" stroke="#666" stroke-width="1.3"><circle cx="5" cy="5" r="3.8"/><path d="M8 8l3 3"/></svg></span>
  <h4>The Oscar</h4>
  <div class="stars"><svg width="60" height="10" viewBox="0 0 60 10" fill="var(--star)"><use href="#st"/><use href="#st" x="12"/><use href="#st" x="24"/><use href="#st" x="36"/><use href="#st" x="48"/></svg></div>
  <div class="price">$30.99</div>
</article>
<article class="product" style="left:861px">
  <span class="product-img" role="img" aria-label="Beige tufted-back armchair with dark legs"></span>
  <h4>Tufted Back</h4>
  <div class="stars"><svg width="60" height="10" viewBox="0 0 60 10" fill="var(--star)"><use href="#st"/><use href="#st" x="12"/><use href="#st" x="24"/><use href="#st" x="36"/><use href="#st" x="48"/></svg></div>
  <div class="price">$20.99</div>
</article>

<div class="abs slide-arrow" style="left:76px"><svg width="8" height="10" viewBox="0 0 8 10"><path d="M6 1 2 5l4 4" stroke="#fff" stroke-width="1.5" fill="none"/></svg></div>
<div class="abs slide-arrow" style="left:1092px"><svg width="8" height="10" viewBox="0 0 8 10"><path d="M2 1l4 4-4 4" stroke="#fff" stroke-width="1.5" fill="none"/></svg></div>

<i class="abs rule"></i>
<div class="badge" style="left:116px" aria-label="Partner badge"></div>
<div class="badge square" style="left:296px" aria-label="Partner badge"></div>
<div class="badge" style="left:473px" aria-label="Partner badge"></div>
<div class="badge square" style="left:651px" aria-label="Partner badge"></div>
<div class="badge square" style="left:829px" aria-label="Partner badge"></div>
<div class="badge" style="left:1005px" aria-label="Partner badge"></div>

<section class="abs newsletter">
  <h2>Subscribe to our Newsletter</h2>
  <form><span class="field">Enter your email address</span><span class="submit">Subscribe</span></form>
</section>

<footer>
  <div class="footer-col" style="left:86px"><h5>My Account</h5><ul><li>My Orders</li><li>My Vouchers</li><li>My Address</li><li>My Credit Slip</li><li>My History</li></ul></div>
  <div class="footer-col" style="left:323px"><h5>Information</h5><ul><li>Contact Us</li><li>Search Terms</li><li>Shipping Guide</li><li>Term Of Use</li><li>Affiliate</li></ul></div>
  <div class="footer-col" style="left:567px"><h5>Extra</h5><ul><li>Brand Partners</li><li>Gift Vouchers</li><li>Specials</li><li>Promotions</li><li>Whishlist</li></ul></div>
  <div class="footer-col" style="left:790px"><h5>Collection</h5><ul><li>Decorations</li><li>Living Room</li><li>Specials</li><li>Offical Care</li><li>Kitchen Care</li></ul></div>
  <div class="footer-col social" style="left:1021px"><h5>Follow Us</h5><ul>
    <li><i class="dot" style="background:#3b5a99"></i>Circlevo</li>
    <li><i class="dot" style="background:#2aa8e0"></i>Chirpa</li>
    <li><i class="dot" style="background:#d93b2b"></i>Seekwave +</li>
    <li><i class="dot" style="background:#1d4f7c"></i>Workvane</li>
  </ul></div>
  <i class="abs footer-rule"></i>
  <p class="abs copyright">2017 © Copyright . All rights reserved</p>
  <div class="abs cards">
    <span class="card">Payvesk</span><span class="card">Kardel</span><span class="card">Duomint</span><span class="card">Findova</span><span class="card">Crestvy</span><span class="card">Orbelle</span>
  </div>
</footer>

</body>
</html>
```